Grocery Shopping App In-Store Marketing Materials

I am looking for simple and colorful designs for shelf wobblers (danglers that hang from grocery shelves usually 3"x5" and in the shape of a smartphone) and door clings (6"x9"). I need two options for my shelf wobblers: one marketing our SMS text marketing platform that will be used to promote VIP deals, coupons, and specials. The other wobbler to market the benefits of our shopping app which includes great recipes, coupons, grocery list creator, and weekly e-mail newsletter called Stir&Snip.com. The door clings will mirror the shelf wobblers. I have included files to help with inspiration. The final design should focus on communicating with a good mix of text and icons to drive the point home. I would also like a poster design to hang from store ceilings.

Target Market(s)

Grocery shoppers

Industry/Entity Type

Marketing

Colors
f04a51
fbee3f
3276b5
abd037

Requirements
Must have
• rock star appeal
Nice to have
• Since we are a mobile app for grocery I would like to see solid color scheme that jumps out or pics of produce, etc.

```html
<!DOCTYPE html>
<html lang="en">
<head>
<meta charset="utf-8">
<title>Spring Sale Poster – Stir&amp;Snip</title>
<link rel="stylesheet" href="https://fonts.googleapis.com/css2?family=Anton&family=Bowlby+One&family=Lobster&family=Open+Sans:wght@400;600;700&display=swap">
<style>
  :root {
    --frame-blue: #3784e6;
    --panel-yellow: #f4f532;
    --hot-red: #f0325a;
    --lime: #a6ff00;
    --ink: #333333;
    --white: #ffffff;
  }
  * { margin: 0; padding: 0; box-sizing: border-box; }
  html, body { width: 807px; height: 1200px; overflow: hidden; background: var(--frame-blue); }
  .poster {
    position: relative;
    width: 807px; height: 1200px;
    background: var(--frame-blue);
    font-family: "Open Sans", Arial, sans-serif;
  }
  .headline-band {
    position: absolute; top: 0; left: 0; width: 100%; height: 143px;
    display: flex; align-items: center; justify-content: center;
    color: var(--white);
    font-size: 84px; font-weight: 400; letter-spacing: 1px;
  }
  .sale-panel {
    position: absolute; top: 143px; left: 16px; width: 775px; height: 1043px;
    background: var(--panel-yellow);
  }
  .big-offer { position: absolute; top: 0; left: 0; }
  .season-line {
    position: absolute; top: 612px; left: 0; width: 100%;
    text-align: center; font-size: 64px; font-weight: 600; letter-spacing: 1px;
  }
  .season-line .word-special { color: var(--hot-red); }
  .season-line .word-springs { color: var(--frame-blue); }
  .discount-bar {
    position: absolute; top: 709px; left: 164px; width: 445px; height: 73px;
    background: linear-gradient(90deg, var(--hot-red) 0 50%, var(--frame-blue) 50% 100%);
    color: var(--panel-yellow);
    font-size: 64px; font-weight: 600; line-height: 73px; text-align: center; letter-spacing: 1px;
  }
  .code-label {
    position: absolute; top: 842px; left: 50px; width: 346px;
    color: var(--hot-red); font-size: 40px; font-weight: 600; text-align: center;
  }
  .code-box {
    position: absolute; top: 897px; left: 50px; width: 346px; height: 100px;
    border: 1.5px dashed var(--frame-blue);
    display: flex; align-items: center; justify-content: center;
    color: var(--frame-blue); font-size: 58px; font-weight: 400;
    text-shadow: -2px -2px 0 var(--hot-red);
  }
  .store-callout {
    position: absolute; top: 800px; left: 490px; width: 240px;
    color: var(--ink); font-family: "Lobster", cursive; font-size: 58px; text-align: center;
  }
  .store-name {
    position: absolute; top: 918px; left: 500px; width: 220px;
    color: var(--hot-red); font-size: 40px; font-weight: 700; text-align: center;
  }
</style>
</head>
<body>
<main class="poster">
  <header class="headline-band">NEW DEAL!!!!!</header>
  <section class="sale-panel">
    <svg class="big-offer" width="775" height="580" viewBox="0 0 775 580" aria-label="50% Sale">
      <text x="118" y="292" font-family="Bowlby One, sans-serif" font-size="300" textLength="512" lengthAdjust="spacingAndGlyphs" fill="var(--frame-blue)">50%</text>
      <text x="124" y="297" font-family="Bowlby One, sans-serif" font-size="300" textLength="512" lengthAdjust="spacingAndGlyphs" fill="var(--hot-red)">50%</text>
      <text x="129" y="557" font-family="Anton, sans-serif" font-size="290" textLength="495" lengthAdjust="spacingAndGlyphs" fill="var(--lime)" stroke="var(--hot-red)" stroke-width="1.5" stroke-dasharray="2 3">SALE</text>
    </svg>
    <p class="season-line"><span class="word-special">SPECIAL</span> <span class="word-springs">SPRINGS</span></p>
    <p class="discount-bar">DISCOUNT</p>
    <p class="code-label">DISCOUNT CODE</p>
    <p class="code-box">SPRING50</p>
    <p class="store-callout">Only at</p>
    <p class="store-name">Stir&amp;Snip</p>
  </section>
</main>
</body>
</html>
```